Recruitment Flyer for Larkfield Lending company

Larkfield Lending centre requires a four page A4 color brochure for new staff who will be joining the organisation.

The brochure is received during the interview for the job role. so we are looking for nice glossy pictures combined with sufficient text to enable the applicant to make an informed decision.

I have attached a word document that may help plus lots of pictures that are on the website that could be used also.

Target Market(s)

New staff joining the organisation

Industry/Entity Type

Mortgage

Font styles to use
Sans Serif

Colors
3377b5
6b449b
b768aa
34a6d7

Requirements
Must have
• Glossy, colorful and career happy
Nice to have
• lots of photos and opportunity for text
Should not have
• be sad or not happy

```html
<!DOCTYPE html>
<html lang="en">
<head>
<meta charset="utf-8">
<title>Larkfield Lending – Staff Brochure</title>
<link rel="stylesheet" href="https://fonts.googleapis.com/css2?family=Oswald:wght@500&family=Raleway:wght@400;500;700&display=swap">
<style>
  :root {
    --purple: #6b449b;
    --number: #5b4a9e;
    --mauve: #b768aa;
    --blue: #3377b5;
    --sky: #34a6d7;
    --teal: #2f8fa8;
    --ink: #4a4a55;
    --paper: #ffffff;
    --paper-shade: #f1f2f5;
    --gutter: #e2e4ea;
    --backdrop: #e4e4e8;
  }
  * { box-sizing: border-box; margin: 0; padding: 0; }
  html, body { width: 1200px; height: 729px; overflow: hidden; }
  body {
    background: var(--backdrop);
    font-family: "Raleway", Arial, sans-serif;
    position: relative;
  }

  /* ---------- Inner spread ---------- */
  .spread {
    position: absolute; left: 40px; top: 114px;
    width: 700px; height: 500px;
    background: linear-gradient(90deg, var(--paper) 0%, var(--paper-shade) 46%, var(--gutter) 50%, var(--paper-shade) 54%, var(--paper) 100%);
    box-shadow: 0 6px 18px rgba(0,0,0,.18);
    overflow: hidden;
  }
  .photo-strip { display: flex; height: 158px; }
  .photo { height: 100%; }
  .photo--desk { width: 200px; background: linear-gradient(160deg, #d9d6d3, #9f98a0 60%, #6e6573); }
  .photo--band { width: 28px; background: var(--purple); opacity: .92; }
  .photo--window { width: 62px; background: linear-gradient(180deg, #8b7ea8, #5e4f80); }
  .photo--meeting { width: 165px; background: linear-gradient(170deg, #c9c8cc, #7b7683 55%, #3f3a48); }
  .photo--volunteers { width: 160px; background: linear-gradient(160deg, #7e8a5f, #8c6aa8 55%, #6b449b); }
  .photo--seniors { width: 85px; background: linear-gradient(170deg, #9d86b8, #6b5388); }

  .point { position: absolute; display: flex; align-items: flex-start; }
  .point__number {
    font-family: "Oswald", "Arial Narrow", sans-serif;
    font-weight: 500; font-size: 46px; line-height: 44px;
    color: var(--number); width: 38px; flex: none;
  }
  .point__text {
    font-size: 6.4px; line-height: 8.2px; color: var(--ink);
    width: 222px; margin-left: 4px;
  }
  .col-left { left: 48px; }
  .col-right { left: 398px; }
  .row-1 { top: 184px; }
  .row-2 { top: 264px; }
  .row-3 { top: 344px; }

  .adviser-photo {
    position: absolute; left: 318px; top: 342px; width: 68px; height: 108px;
    background: linear-gradient(180deg, #ddd3d0 0%, #c9c3cf 60%, #e6e7ec 100%);
  }
  .spread__footer {
    position: absolute; left: 0; bottom: 0; width: 100%; height: 22px;
    background: var(--purple);
  }

  /* ---------- Cover ---------- */
  .cover {
    position: absolute; left: 790px; top: 114px;
    width: 370px; height: 500px;
    background: var(--paper);
    box-shadow: 0 6px 18px rgba(0,0,0,.18);
    overflow: hidden;
  }
  .cover svg { display: block; }
  .brand {
    position: absolute; left: 26px; top: 26px;
    display: flex; align-items: center; gap: 8px;
  }
  .brand__dot { width: 18px; height: 18px; border-radius: 50%; background: var(--blue); }
  .brand__name {
    font-family: "Raleway", Arial, sans-serif; font-weight: 500;
    font-size: 20px; color: var(--blue); letter-spacing: .3px;
  }
  .tagline {
    position: absolute; left: 78px; top: 316px; color: #fff;
    font-family: "Raleway", Arial, sans-serif;
  }
  .tagline__lead { display: block; font-size: 29px; font-weight: 500; line-height: 32px; }
  .tagline__rest { display: block; font-size: 19px; font-weight: 400; margin-left: 18px; }
  .tagline__rest strong { font-weight: 700; }
</style>
</head>
<body>

<section class="spread" aria-label="Inner spread">
  <div class="photo-strip">
    <div class="photo photo--desk" role="img" aria-label="Photo of a staff member relaxing at a desk with laptop and paperwork"></div>
    <div class="photo photo--band"></div>
    <div class="photo photo--window" role="img" aria-label="Photo of an office window tinted purple"></div>
    <div class="photo photo--meeting" role="img" aria-label="Photo of two colleagues reviewing documents in a meeting"></div>
    <div class="photo photo--volunteers" role="img" aria-label="Photo of smiling volunteers working together outdoors"></div>
    <div class="photo photo--seniors" role="img" aria-label="Photo of older community members, tinted purple"></div>
  </div>

  <div class="point col-left row-1"><span class="point__number">1</span><p class="point__text">"Welcome to Larkfield Lending. We help local families find the right home loan, and our people are the reason they trust us. From your first day you will join a friendly team that shares knowledge, celebrates wins and supports each other every step."</p></div>
  <div class="point col-left row-2"><span class="point__number">2</span><p class="point__text">"Your first weeks include a full induction with a dedicated mentor. You will learn our lending products, systems and customer standards, then shadow experienced advisers before taking on your own clients with confidence and plenty of guidance along the way."</p></div>
  <div class="point col-left row-3"><span class="point__number">3</span><p class="point__text">"Training never stops here. We fund recognised mortgage qualifications, run regular workshops and offer clear career paths, so whether you start in customer service or processing, you can grow into advice, team leadership or specialist roles over time."</p></div>

  <div class="adviser-photo" role="img" aria-label="Photo of a customer adviser wearing a headset"></div>

  <div class="point col-right row-1"><span class="point__number">4</span><p class="point__text">"We believe good work deserves good rewards. Our package includes a competitive salary, performance bonuses, generous annual leave, a pension scheme and health cover, plus a paid volunteering day so you can give back to the community you serve."</p></div>
  <div class="point col-right row-2"><span class="point__number">5</span><p class="point__text">"Flexible working helps our people balance life and career. Many roles offer hybrid hours, and our bright, modern centre has quiet spaces, shared kitchens and meeting rooms designed for teams to plan, learn and solve problems together."</p></div>
  <div class="point col-right row-3"><span class="point__number">6</span><p class="point__text">"Ready to take the next step? Ask your interviewer any questions today, talk with the team about daily life here, and take this brochure home. We look forward to welcoming you and helping you build a happy, rewarding career."</p></div>

  <div class="spread__footer"></div>
</section>

<section class="cover" aria-label="Front cover">
  <svg width="370" height="500" viewBox="0 0 370 500">
    <defs>
      <linearGradient id="handsTone" x1="0" y1="0" x2="1" y2="1">
        <stop offset="0" stop-color="#f3d79a"/>
        <stop offset=".45" stop-color="#c9967a"/>
        <stop offset="1" stop-color="#7a5a5c"/>
      </linearGradient>
    </defs>
    <polygon points="0,130 370,22 370,392 0,392" fill="url(#handsTone)" role="img" aria-label="Photo of team members stacking their hands together"/>
    <polygon points="0,112 225,70 0,250" fill="var(--purple)" opacity=".9"/>
    <polygon points="0,370 370,178 370,392 0,392" fill="var(--teal)" opacity=".95"/>
    <text x="50" y="338" fill="#fff" opacity=".55" font-family="Raleway, Arial, sans-serif" font-size="46" font-weight="700">“</text>
    <text x="302" y="400" fill="#fff" opacity=".55" font-family="Raleway, Arial, sans-serif" font-size="46" font-weight="700">”</text>
  </svg>
  <div class="brand"><span class="brand__dot"></span><span class="brand__name">Larkfield Lending</span></div>
  <p class="tagline"><span class="tagline__lead">Team work</span><span class="tagline__rest">makes <strong>Dream work</strong></span></p>
</section>

</body>
</html>
```